Need cover for book about the Slow Snare child sex traffickers play with their victims

We train professionals, first responders, parents, foster parents, and others about child sex trafficking in the United States. This book is based on the life story of a former 32-year child sex trafficker who sold more than 150 children and women in all 50 states, Canada, and Europe. The book will not only help prevent kids from becoming victims of people like he was, but it also will prevent youth from becoming traffickers, as well.

```html
<!DOCTYPE html>
<html lang="en">
<head>
<meta charset="utf-8">
<title>Slow Snare – Book Cover</title>
<link href="https://fonts.googleapis.com/css2?family=Tinos:wght@400&family=Arimo:wght@400&display=swap" rel="stylesheet">
<style>
  :root {
    --backdrop: #7a7a7a;
    --silver-light: #e9e9e9;
    --silver-mid: #a9a9a9;
    --silver-dark: #6f6f6f;
    --copper-light: #f2a531;
    --copper-mid: #c56a12;
    --copper-dark: #5a2a06;
    --ink: #111111;
    --subtitle-ink: #4a4a4a;
  }
  html, body {
    margin: 0;
    padding: 0;
    width: 833px;
    height: 1200px;
    overflow: hidden;
    background: var(--backdrop);
  }
  .book-cover {
    position: relative;
    width: 833px;
    height: 1200px;
    overflow: hidden;
    background:
      radial-gradient(ellipse at 70% 25%, var(--copper-light) 0%, transparent 55%),
      radial-gradient(ellipse at 85% 85%, var(--copper-dark) 0%, transparent 50%),
      linear-gradient(160deg, var(--copper-mid) 0%, #d98422 45%, var(--copper-mid) 75%, var(--copper-dark) 100%);
  }
  .silver-band {
    position: absolute;
    left: 0;
    top: 0;
    width: 330px;
    height: 100%;
    background:
      radial-gradient(ellipse at 40% 20%, var(--silver-light) 0%, transparent 60%),
      radial-gradient(ellipse at 60% 75%, #d6d6d6 0%, transparent 55%),
      linear-gradient(175deg, #cfcfcf 0%, var(--silver-mid) 40%, #bdbdbd 65%, var(--silver-dark) 100%);
  }
  .title-block {
    position: absolute;
    left: 60px;
    top: 170px;
    margin: 0;
    color: var(--ink);
    font-family: "Tinos", "Times New Roman", serif;
    font-weight: 400;
    text-transform: uppercase;
  }
  .title-line {
    display: block;
    font-size: 170px;
    line-height: 0.82;
    letter-spacing: -3px;
    white-space: nowrap;
  }
  .title-line--first { margin-left: 40px; }
  .title-line--second { margin-left: 0; }
  .subtitle {
    position: absolute;
    left: 100px;
    top: 478px;
    margin: 0;
    font-family: "Arimo", Arial, sans-serif;
    font-weight: 400;
    font-size: 22px;
    color: var(--subtitle-ink);
    white-space: nowrap;
  }
  .credits {
    position: absolute;
    right: 40px;
    bottom: 110px;
    width: 620px;
    text-align: right;
    font-family: "Arimo", Arial, sans-serif;
    font-size: 16px;
    line-height: 1.3;
    color: var(--ink);
  }
  .credits p { margin: 0; }
</style>
</head>
<body>
  <main class="book-cover">
    <div class="silver-band" role="img" aria-label="Silver marbled texture panel"></div>

    <h1 class="title-block">
      <span class="title-line title-line--first">Slow</span>
      <span class="title-line title-line--second">Snare</span>
    </h1>

    <p class="subtitle">Inside the Quiet Tactics of Coercive Control</p>

    <div class="credits">
      <p>Dr. Lena Marsh and Victor Hale, a former 32-year child sex trafficker</p>
      <p>With forward by Renee Hale, Victor's longtime victim and bottom</p>
      <p>And creator of the Safe Path program.</p>
    </div>
  </main>
</body>
</html>
```